Modern Design Business Card industrial maintenance company

Business card design for Company named Brookvale Equipment Services

Target Market(s)

Industrial

Industry/Entity Type

Maintenance and repair

Contact Information for Business Card

Place holder for address, office phone, mobile number and email

Requirements
Must have
• Clean modern look
Nice to have
• N/a

```html
<!DOCTYPE html>
<html lang="en">
<head>
<meta charset="utf-8">
<title>Brookvale Equipment Services — Business Card</title>
<link href="https://fonts.googleapis.com/css2?family=Montserrat:wght@400;500;600&display=swap" rel="stylesheet">
<style>
  :root {
    --backdrop: #3a3a3c;
    --card-light: #ffffff;
    --card-dark: #1c1c1d;
    --ink: #1a1a1a;
    --silver: #bdbdbd;
    --font: "Montserrat", Arial, sans-serif;
  }
  * { margin: 0; padding: 0; box-sizing: border-box; }
  html, body {
    width: 1200px; height: 1200px; overflow: hidden;
    background: var(--backdrop);
    font-family: var(--font);
  }
  .canvas { position: relative; width: 1200px; height: 1200px; }
  .card {
    position: absolute; left: 210px;
    width: 780px; height: 446px;
    border-radius: 34px;
    overflow: hidden;
  }
  .card--front { top: 100px; background: var(--card-light); color: var(--ink); }
  .card--back { top: 654px; background: var(--card-dark); }

  /* front: brand block */
  .brand {
    position: absolute; left: 56px; top: 120px; width: 320px;
    display: flex; flex-direction: column; align-items: flex-start; gap: 18px;
  }
  .brand__mark {
    width: 92px; height: 92px; border-radius: 50%;
    border: 5px solid var(--ink); margin-left: 40px;
  }
  .brand__name {
    font-weight: 600; font-size: 22px; line-height: 1.2;
    letter-spacing: 1.5px; text-transform: uppercase; color: var(--ink);
    white-space: nowrap;
  }

  /* front: contact block */
  .contact { position: absolute; left: 440px; top: 110px; width: 300px; }
  .contact__name { font-weight: 600; font-size: 38px; letter-spacing: 0.5px; line-height: 1; }
  .contact__role { font-weight: 400; font-size: 17px; letter-spacing: 1px; margin: 6px 0 18px 2px; }
  .contact__list { list-style: none; }
  .contact__item {
    display: flex; align-items: flex-start; gap: 10px;
    font-size: 16px; line-height: 1.25; margin-bottom: 7px;
  }
  .contact__icon { width: 16px; height: 18px; flex: none; margin-top: 1px; fill: var(--ink); }

  /* back */
  .back-brand {
    position: absolute; inset: 0;
    display: flex; flex-direction: column; align-items: center; justify-content: center;
    gap: 26px;
  }
  .back-brand__mark { width: 150px; height: 150px; border-radius: 50%; border: 5px solid var(--silver); }
  .back-brand__name {
    font-weight: 600; font-size: 34px; letter-spacing: 3px;
    text-transform: uppercase; color: var(--silver); text-align: center; line-height: 1.2;
  }
</style>
</head>
<body>
<main class="canvas">
  <section class="card card--front">
    <div class="brand">
      <span class="brand__mark"></span>
      <p class="brand__name">Brookvale<br>Equipment Services</p>
    </div>

    <div class="contact">
      <h1 class="contact__name">FULL NAME</h1>
      <p class="contact__role">POSITION</p>
      <ul class="contact__list">
        <li class="contact__item">
          <svg class="contact__icon" viewBox="0 0 16 18"><path d="M3 1l3 0 1.5 4-2 1.5c1 2.2 2.6 3.8 4.8 4.8L11.8 9.3l4 1.5v3c0 1-1 2-2 2C7 15.5 1 9.5 1 3c0-1 1-2 2-2z"/></svg>
          <span>(000) 000 0000</span>
        </li>
        <li class="contact__item">
          <svg class="contact__icon" viewBox="0 0 16 18"><path d="M4 0h8a2 2 0 0 1 2 2v14a2 2 0 0 1-2 2H4a2 2 0 0 1-2-2V2a2 2 0 0 1 2-2zm0 2v12h8V2zm3 13.2h2v1.3H7z"/></svg>
          <span>(000) 000 0000</span>
        </li>
        <li class="contact__item">
          <svg class="contact__icon" viewBox="0 0 16 18"><path d="M0 4h16v11H0zm1.5 1.5L8 10l6.5-4.5z"/></svg>
          <span>email@company.com</span>
        </li>
        <li class="contact__item">
          <svg class="contact__icon" viewBox="0 0 16 18"><path d="M8 0a6 6 0 0 1 6 6c0 4.5-6 12-6 12S2 10.5 2 6a6 6 0 0 1 6-6zm0 3.5a2.5 2.5 0 1 0 0 5 2.5 2.5 0 0 0 0-5z"/></svg>
          <span>123 Name Street, 000<br>Your City, 00000-000</span>
        </li>
      </ul>
    </div>
  </section>

  <section class="card card--back">
    <div class="back-brand">
      <span class="back-brand__mark"></span>
      <p class="back-brand__name">Brookvale<br>Equipment Services</p>
    </div>
  </section>
</main>
</body>
</html>
```